Building company with a modern and unique product looking for a business card to help us stand out

We currently have a logo but as our business has grown, we feel that our business card is not reflecting our modern and high quality product and help us stand out from the crowd. Our business is mainly in the construction of new homes using a unique method and materials that makes our homes fire proof, vermin and pest resistant and rated to the maximum cyclone category (category 5). We need a business card that helps us stand out as well as communicating professionalism, high quality and trustworthiness. I have attached our current logo with a black and white option, as well as our business card which is double sided. We would like to retain as much of the information that is currently on our business cards, but presented in a more sleek way. We do like our current colour palette ( white, black, yellow and grey) and have been looking primarily at business cards with a black background however we are open to other combinations of colour and layout as long as we stand out. Please feel free to tweak our logo to make it more suitable for a business card, we like the black option that we use but we have had trouble trying to get the white area to match the rest of the logo and blend effectively into a business card. Please do not hesitate to contact us with any questions as we really want this to be successful!

Target Market(s)

Large contracts including government and larger companies

Industry/Entity Type

Business

We will be providing this business card to potential clients including key government ministers and large funding companies, our business card should show that we are professional and reliable.

Requirements
Must have
• It must be easy to read and pleasing to the eye, It must contain as much of the information on the current business card and unless something really stands out, we will most likely pick a design that has all of the information included. It must include our logo of course and have some colour included.
Nice to have
• We are looking for a high end business card and would like to see designs that reflect this. We like the gloss/matte contrast, plastic cards with opaque/coloured areas and unique features not seen on everyday paper business cards. It would be nice to see a few different colour combinations, we are open to new ideas so please feel free to take some artistic licence.
Should not have
• Must not be too busy, difficult to read or be distracting from the information conveyed. Other than this please feel free to add your own touches and make it unique!

```html
<!DOCTYPE html>
<html lang="en">
<head>
<meta charset="utf-8">
<title>KRL Building Company – Business Card</title>
<link rel="stylesheet" href="https://fonts.googleapis.com/css2?family=Open+Sans:wght@400;600;700&display=swap">
<style>
  :root {
    --bg: #3b3430;
    --card: #1c1c1c;
    --card-edge: #232323;
    --gold: #d4a928;
    --white: #f2f2f2;
    --grey: #9a9a9a;
  }
  * { margin: 0; padding: 0; box-sizing: border-box; }
  html, body {
    width: 1200px; height: 844px; overflow: hidden;
    background: var(--bg);
    font-family: "Open Sans", Arial, sans-serif;
  }
  .stage {
    position: relative; width: 1200px; height: 844px;
    display: flex; align-items: center; justify-content: center; gap: 50px;
  }
  .card {
    position: relative; width: 520px; height: 316px;
    background: linear-gradient(135deg, var(--card-edge), var(--card) 60%);
    overflow: hidden;
    box-shadow: 0 10px 30px rgba(0,0,0,.45);
  }

  /* Back: contact side */
  .card-back .band {
    position: absolute; left: 0; right: 0; height: 12px; background: var(--gold);
  }
  .card-back .band-top { top: 18px; }
  .card-back .band-bottom { bottom: 18px; }
  .contact {
    position: absolute; top: 74px; left: 0; right: 0;
    text-align: center; color: var(--white);
  }
  .contact .name {
    display: inline-block;
    font-weight: 700; font-size: 19px; letter-spacing: .5px;
    color: var(--gold); text-transform: uppercase;
    padding-bottom: 2px; border-bottom: 1.5px solid var(--gold);
  }
  .contact .role { font-size: 13px; margin-top: 4px; }
  .contact .abn { font-size: 14px; margin-top: 30px; }
  .contact .abn span { color: var(--gold); }
  .contact .lines { font-size: 14px; line-height: 21px; margin-top: 26px; }

  /* Front: brand side */
  .card-front .tab {
    position: absolute; width: 22px; height: 46px; background: var(--gold);
    border-right: 4px solid #cfcfcf;
  }
  .card-front .tab-right { right: 0; top: 20px; border-right: none; border-left: 4px solid #cfcfcf; }
  .card-front .tab-left { left: 0; top: 170px; }
  .brand {
    position: absolute; top: 64px; left: 0; right: 0;
    display: flex; align-items: center; justify-content: center; gap: 12px;
  }
  .brand .mark { width: 18px; height: 18px; background: var(--gold); }
  .brand .wordmark {
    font-weight: 600; font-size: 30px; color: var(--white); letter-spacing: .5px;
  }
  .tagline {
    position: absolute; top: 172px; left: 0; right: 0; text-align: center;
    color: var(--gold); font-weight: 700; font-size: 13px;
  }
  .qualities {
    position: absolute; top: 218px; left: 0; right: 0; text-align: center;
    color: var(--white); font-size: 14px; word-spacing: 2px;
  }
  .qualities .sep { color: var(--grey); margin: 0 8px; }
</style>
</head>
<body>
<main class="stage">
  <section class="card card-back" aria-label="Business card, contact side">
    <div class="band band-top"></div>
    <div class="contact">
      <div class="name">Daniel Morrow</div>
      <div class="role">Managing Director</div>
      <div class="abn"><span>ABN:</span> 48 207 315 662</div>
      <div class="lines">
        0412 357 904<br>
        (02) 61 480 239<br>
        krlbuilding@mailbox.net
      </div>
    </div>
    <div class="band band-bottom"></div>
  </section>

  <section class="card card-front" aria-label="Business card, brand side">
    <div class="tab tab-right"></div>
    <div class="tab tab-left"></div>
    <div class="brand">
      <span class="mark"></span>
      <span class="wordmark">KRL Building Company</span>
    </div>
    <p class="tagline">Specialising in Homes that are</p>
    <p class="qualities">Fire Proof<span class="sep">|</span>Climate Proof<span class="sep">|</span>Cyclone Rated (Cat. 5)</p>
  </section>
</main>
</body>
</html>
```